Real Estate | Property Management Website Design

We are working with a Real Estate company in California. They provide Property Management Services and Real Estate Services.

PLEASE NOT: make sure the site covers real estate and property management).

A few websites for inspiration:
https://pinebrookleases.com
https://www.varmolhomeadvisors.com
https://marisotelvy.com
https://tobenhalvrick.com
https://thecalvenparty.com
https://ronaquistmoor.com
https://zvask.com

Thank you for taking the time to consider designing a website for us. We are web developers based in Stockton, CA, USA. Most of our projects go through the same process. Understanding this process may help you win a project with us. We custom-code all of our websites in-house. We don’t have any requirements as to what tools you use for your design, but we ask that you follow these guidelines.

IMAGES:
If you use any images or icons in the design, we ask that you have a link to the asset so we can purchase the image/icon. Most of the designs we submit do not have the customer’s images on them unless they have some great images. Be creative; show us the feeling you are trying to portray with your image choices. Use any royalty-free site you choose. We subscribe to Plimora and mainly use their images, but we can purchase images outside of Plimora. PLEASE NOTE: we will not submit designs to clients with watermarks on the images.

FONTS:
We ask that you identify the fonts you’re using in the design. This can be done in a message if you want. We typically use Quendle Fonts and Plimora Fonts.

CONTENT:
We're always open to different content and ideas. We often submit designs with stock images so the client can see our vision. We typically take pictures after the website launch to use their images with our vision. Lorem Ipsum is fine for paragraphs, but we ask that you make the Headers with correct English. We want to be able to show the vision and identify the sections of the website.

INSPIRATION:
We typically add a couple of links in the brief of websites we like to help you get started in your design.

REVISIONS:
We do not often ask for revisions of the designs unless we see something in the design that may not appeal to the client. If there are slight changes that we want to make, we do that in the development process.

FEEDBACK:
We rarely give feedback on designs during the design process. We are working on many website projects and do not have the time to provide feedback. We usually respond if your request is well thought out and asks specific questions, but a note asking “feedback, please” usually goes unanswered.

```html
<!DOCTYPE html>
<html lang="en">
<head>
<meta charset="utf-8">
<title>Skyloft Estates – Property Management &amp; Real Estate</title>
<link href="https://fonts.googleapis.com/css2?family=Jost:ital,wght@0,400;0,500;0,600;0,700;1,400&display=swap" rel="stylesheet">
<style>
:root{
  --orange:#f26a23;
  --ink:#1c1c1c;
  --body:#3a3a3a;
  --muted:#8a8a8a;
  --line:#d9d9d9;
  --panel:#f3f3f3;
  --white:#ffffff;
}
*{box-sizing:border-box;margin:0;padding:0}
html,body{width:1200px;height:5141px;overflow:hidden}
body{position:relative;background:var(--white);font-family:"Jost",sans-serif;color:var(--body)}
.abs{position:absolute}
.btn{position:absolute;display:flex;align-items:center;justify-content:center;background:var(--orange);color:var(--white);border-radius:24px;font-weight:600;font-size:13px;letter-spacing:.5px;text-transform:uppercase;white-space:nowrap}
.btn-outline{background:var(--white);color:var(--orange);border:2px solid var(--orange)}
.photo{position:absolute}
h2.section-title{position:absolute;left:0;width:1200px;text-align:center;font-size:42px;font-weight:700;color:var(--ink);letter-spacing:1px}
.center-text{position:absolute;left:220px;width:760px;text-align:center;font-size:15px;line-height:21px;color:var(--ink)}

/* hero */
.hero-photo{left:0;top:0;width:1200px;height:670px;background:linear-gradient(135deg,#1e2530 0%,#3a2e22 35%,#5a4630 55%,#1d3240 80%,#2b4a5b 100%)}
.brand{position:absolute;display:flex;align-items:center;gap:10px;color:var(--orange);font-weight:700;font-size:26px;line-height:24px;text-transform:uppercase}
.brand-mark{width:22px;height:22px;background:var(--orange)}
.nav{position:absolute;top:76px;left:372px;display:flex}
.nav a{color:var(--white);text-decoration:none;font-size:13px;font-weight:500;letter-spacing:.5px;white-space:nowrap}
.hero-title{position:absolute;top:266px;left:0;width:1200px;text-align:center;color:var(--white);font-size:46px;font-weight:500;letter-spacing:2px}

/* about */
.about-line{left:124px;top:706px;width:3px;height:346px;background:var(--orange)}
.about-title{left:150px;top:734px;font-size:42px;font-weight:700;color:var(--ink)}
.about-text{left:150px;width:440px;font-size:13px;line-height:19px;color:var(--body)}
.about-frame{left:664px;top:612px;width:448px;height:508px;background:var(--white)}
.about-photo{left:676px;top:624px;width:424px;height:480px;background:linear-gradient(160deg,#c9cfd4 0%,#9aa4ab 40%,#8a5a3a 70%,#c8b8a6 100%)}

/* services */
.services-band{left:0;top:1228px;width:1200px;height:528px;background:linear-gradient(180deg,#eeeeee 0%,#dcdcdc 55%,#e6e6e6 100%)}
.service-card{position:absolute;top:1536px;width:518px;height:364px}
.service-card span{position:absolute;left:30px;bottom:44px;color:var(--white);font-size:26px;font-weight:600;letter-spacing:1px;text-transform:uppercase;white-space:nowrap}

/* works */
.work-card{position:absolute;top:2256px;width:312px;height:474px;border:1px solid var(--line);background:var(--white)}
.work-card .img{position:absolute;left:0;top:0;width:310px;height:236px}
.work-card h3{position:absolute;left:26px;top:262px;font-size:18px;font-weight:600;color:var(--ink);white-space:nowrap}
.work-card .price{position:absolute;left:26px;top:288px;font-size:18px;font-weight:500;color:var(--orange)}
.work-card p{position:absolute;left:26px;top:322px;width:262px;font-size:12px;line-height:18px;color:var(--muted)}
.work-card .btn{left:47px;top:412px;width:216px;height:44px;font-size:12px}
.arrow-btn{position:absolute;top:2796px;width:44px;height:44px;border:2px solid var(--ink);border-radius:50%;display:flex;align-items:center;justify-content:center}

/* work with us */
.cta-photo{left:0;top:2928px;width:1200px;height:524px;background:linear-gradient(120deg,#3e4d58 0%,#6b7a80 30%,#c9b8a0 55%,#8a6a46 75%,#3b3a36 100%)}
.cta-title{position:absolute;top:3160px;left:0;width:1200px;text-align:center;color:var(--white);font-size:48px;font-weight:700;letter-spacing:1px}

/* testimonials */
.quote{position:absolute;left:250px;width:700px;text-align:center;font-style:italic;font-size:17px;line-height:23px;color:var(--body)}
.person{position:absolute;left:0;width:1200px;text-align:center}

/* contact */
.contact-panel{left:0;top:4036px;width:492px;height:576px;background:linear-gradient(180deg,#f26a23 0%,#ef6420 100%)}
.contact-form-bg{left:492px;top:4036px;width:708px;height:576px;background:var(--panel)}
.info-head{position:absolute;left:150px;display:flex;align-items:center;gap:6px;color:var(--white);font-size:18px;font-weight:600;text-transform:uppercase}
.info-text{position:absolute;left:150px;color:var(--white);font-size:12px;line-height:16px;opacity:.9}
.get-title{left:548px;top:4094px;font-size:42px;font-weight:700;color:var(--ink)}
.field{position:absolute;background:#e6e6e6;border:1px solid #dcdcdc;font-size:13px;color:#555;padding:14px}

/* footer */
.foot-col{position:absolute;top:4728px}
.foot-col h4{font-size:15px;font-weight:600;color:var(--ink);margin-bottom:10px;letter-spacing:.5px}
.foot-col li{list-style:none;font-size:12px;line-height:21px;color:var(--body)}
.social{position:absolute;top:4819px;width:32px;height:32px;border:1.5px solid var(--ink);border-radius:50%}
</style>
</head>
<body>

<!-- Hero -->
<div class="photo hero-photo" role="img" aria-label="Modern luxury home at dusk with lit interior and pool terrace"></div>
<div class="brand" style="left:106px;top:64px"><span class="brand-mark"></span>Skyloft<br>Estates</div>
<nav class="nav">
  <a style="margin-right:52px">HOME</a>
  <a style="margin-right:52px">SERVICES</a>
  <a style="margin-right:52px">RENTAL SEARCH</a>
  <a style="margin-right:52px">ABOUT</a>
  <a>CONTACT</a>
</nav>
<div class="btn" style="left:930px;top:62px;width:166px;height:44px">Schedule a call</div>
<h1 class="hero-title">SKYLOFT ESTATES</h1>
<div class="btn" style="left:518px;top:344px;width:166px;height:44px">Schedule a call</div>

<!-- About -->
<div class="abs about-line"></div>
<h2 class="abs about-title">ABOUT US</h2>
<p class="abs about-text" style="top:806px">Lorem ipsum dolor sit amet, consectetur adipiscing elit, sed do eiusmod tempor incididunt ut labore et dolore magna aliqua. Quis ipsum suspendisse ultrices gravida. Risus commodo viverra maecenas accumsan lacus vel facilisis.</p>
<p class="abs about-text" style="top:906px">Lorem ipsum dolor sit amet, consectetur adipiscing elit, sed do eiusmod tempor incididunt ut labore et dolore magna aliqua. Quis ipsum suspendisse ultrices gravida. Risus commodo viverra maecenas accumsan lacus vel facilisis.</p>
<div class="btn" style="left:150px;top:1004px;width:130px;height:44px;font-size:12px">Read more</div>
<div class="abs about-frame"></div>
<div class="photo about-photo" role="img" aria-label="Smiling property agent holding a tablet in a bright office"></div>

<!-- Services -->
<div class="abs services-band" role="img" aria-label="Faded city skyline backdrop"></div>
<h2 class="section-title" style="top:1324px">OUR SERVICES</h2>
<p class="center-text" style="top:1404px">Lorem ipsum dolor sit amet, consectetur adipiscing elit, sed do eiusmod tempor incididunt ut labore et dolore magna aliqua. Quis ipsum suspendisse ultrices gdipiscing elit, sed do eiusmod tempor incididunt ut labore et dolore magna aliquauis ipsum suspendisse ultricesa.</p>
<div class="service-card" style="left:74px;background:linear-gradient(135deg,#3a4150 0%,#6b5a4c 40%,#2c3a55 100%)" role="img" aria-label="Property manager meeting a client"><span>Property Management Services</span></div>
<div class="service-card" style="left:608px;background:linear-gradient(180deg,#3f5a78 0%,#8a94a0 50%,#4f6a38 100%)" role="img" aria-label="Two-storey family house with front porch and garden"><span style="left:118px">Real Estate Services</span></div>

<!-- Property works -->
<h2 class="section-title" style="top:2084px">OUR PROPERTY WORKS</h2>
<p class="center-text" style="top:2160px">Lorem ipsum dolor sit amet, consectetur adipiscing elit, sed do eiusmod tempor incididunt ut labore et dolore magna aliqua. Quis ipsum suspendisse ultrices gdipiscing eli</p>

<div class="work-card" style="left:98px">
  <div class="img" style="background:linear-gradient(180deg,#4a6f9c 0%,#b9a58c 55%,#3f5a2c 100%)" role="img" aria-label="Modern villa with lawn at sunset"></div>
  <h3>Lorem ipsum dolor loresit</h3><div class="price">$ 895700</div>
  <p>Lorem ipsum dolor sit amet, conse ctetur adipiscing elit, sed do eiusmod tempor incididunt ut labore.</p>
  <div class="btn btn-outline">Read more</div>
</div>
<div class="work-card" style="left:446px">
  <div class="img" style="background:linear-gradient(180deg,#dfe3e6 0%,#e8e4dc 50%,#5a7040 100%)" role="img" aria-label="White contemporary townhouse with plants"></div>
  <h3>Lorem ipsum dolor loresit</h3><div class="price">$ 895700</div>
  <p>Lorem ipsum dolor sit amet, conse ctetur adipiscing elit, sed do eiusmod tempor incididunt ut labore.</p>
  <div class="btn btn-outline">Read more</div>
</div>
<div class="work-card" style="left:792px">
  <div class="img" style="background:linear-gradient(180deg,#2f5d9a 0%,#3a5a4a 45%,#1e6a9a 100%)" role="img" aria-label="Resort pool with palm trees"></div>
  <h3>Lorem ipsum dolor loresit</h3><div class="price">$ 895700</div>
  <p>Lorem ipsum dolor sit amet, conse ctetur adipiscing elit, sed do eiusmod tempor incididunt ut labore.</p>
  <div class="btn btn-outline">Read more</div>
</div>
<div class="arrow-btn" style="left:552px"><svg width="14" height="14" viewBox="0 0 14 14"><path d="M9 2 L4 7 L9 12" fill="none" stroke="#1c1c1c" stroke-width="2"/></svg></div>
<div class="arrow-btn" style="left:604px"><svg width="14" height="14" viewBox="0 0 14 14"><path d="M5 2 L10 7 L5 12" fill="none" stroke="#1c1c1c" stroke-width="2"/></svg></div>

<!-- Work with us -->
<div class="photo cta-photo" role="img" aria-label="Contemporary two-storey house with glass walls and wooden slats at dusk"></div>
<h2 class="cta-title">WORK WITH US</h2>
<div class="btn" style="left:518px;top:3248px;width:166px;height:44px;font-size:12px">Contact us</div>

<!-- Testimonials -->
<h2 class="section-title" style="top:3598px;font-size:38px">TESTIMONIALS</h2>
<svg class="abs" style="left:562px;top:3686px" width="76" height="52" viewBox="0 0 76 52"><g fill="none" stroke="#1c1c1c" stroke-width="4"><circle cx="18" cy="16" r="13"/><path d="M31 16 C31 34 22 44 8 49"/><circle cx="55" cy="16" r="13"/><path d="M68 16 C68 34 59 44 45 49"/></g></svg>
<p class="quote" style="top:3760px">Lorem ipsum dolor sit amet, consectetur adipiscing elit, sed do eiusmod tempor incididunt ut labore et dolore magna aliqua. Quis ipsum suspendisse ultrices gravida. Risus commodo viverra maecenas accumsan lacu</p>
<svg class="abs" style="left:150px;top:3768px" width="20" height="30" viewBox="0 0 20 30"><path d="M16 2 L4 15 L16 28" fill="none" stroke="#1c1c1c" stroke-width="3"/></svg>
<svg class="abs" style="left:984px;top:3768px" width="20" height="30" viewBox="0 0 20 30"><path d="M4 2 L16 15 L4 28" fill="none" stroke="#1c1c1c" stroke-width="3"/></svg>
<div class="person" style="top:3852px;color:var(--orange);font-size:20px;font-weight:600">Jesika Loremm</div>
<div class="person" style="top:3878px;color:var(--muted);font-size:15px;font-weight:500">Buyer</div>

<!-- Contact -->
<div class="abs contact-panel" role="img" aria-label="Orange-tinted city skyline"></div>
<div class="abs contact-form-bg"></div>

<div class="info-head" style="top:4150px"><svg width="14" height="18" viewBox="0 0 14 18"><path d="M7 0 C3 0 0 3 0 7 C0 12 7 18 7 18 C7 18 14 12 14 7 C14 3 11 0 7 0Z" fill="#fff"/><circle cx="7" cy="7" r="2.6" fill="#f26a23"/></svg>Address</div>
<div class="info-text" style="top:4188px">218 - 222 W. Marrow Lane<br>Brindle Valley, CA 00000</div>

<div class="info-head" style="top:4282px"><svg width="18" height="18" viewBox="0 0 18 18"><path d="M4 1 L7 5 L5 7 C6 10 8 12 11 13 L13 11 L17 14 L15 17 C8 17 1 10 1 3Z" fill="#fff"/></svg>Phone Number</div>
<div class="info-text" style="top:4320px">Toll-Free: 1-800-555-0142<br>Fax: 1-800-555-0187</div>

<div class="info-head" style="top:4410px"><svg width="18" height="14" viewBox="0 0 18 14"><rect width="18" height="14" rx="1" fill="#fff"/><path d="M1 1 L9 8 L17 1" fill="none" stroke="#f26a23" stroke-width="1.6"/></svg>Email</div>
<div class="info-text" style="top:4448px">info@skyloftestates.com<br>help@skyloftestates.com</div>

<h2 class="abs get-title">GET IN TOUCH</h2>
<p class="abs" style="left:554px;top:4178px;width:520px;font-size:15px;line-height:21px;color:var(--ink)">Lorem ipsum dolor sit amet, consectetur adipiscing elit, sed do eiusmod tempor incididunt ut labore et dolore magna .</p>
<div class="field" style="left:554px;top:4246px;width:238px;height:44px">Name:</div>
<div class="field" style="left:804px;top:4246px;width:238px;height:44px">Email:</div>
<div class="field" style="left:554px;top:4304px;width:238px;height:44px">Phone:</div>
<div class="field" style="left:804px;top:4304px;width:238px;height:44px">Subject</div>
<div class="field" style="left:554px;top:4362px;width:488px;height:124px">Message:</div>
<div class="btn" style="left:556px;top:4508px;width:146px;height:50px;font-size:15px;border-radius:26px">Submit</div>

<!-- Footer -->
<div class="brand" style="left:152px;top:4732px"><span class="brand-mark"></span>Skyloft<br>Estates</div>
<div class="social" style="left:174px"></div>
<div class="social" style="left:222px"></div>
<div class="social" style="left:270px"></div>
<div class="social" style="left:318px"></div>

<div class="foot-col" style="left:480px"><h4>LINKS</h4><ul><li>Home</li><li>Services</li><li>Properties</li><li>Blog</li><li>Contact</li></ul></div>
<div class="foot-col" style="left:642px"><h4>PROPERTIES</h4><ul><li>Latest Properties</li><li>Sales</li><li>Rentals</li><li>Recent Sales</li></ul></div>
<div class="foot-col" style="left:830px"><h4>SERVICES</h4><ul><li>Property Management Services</li><li>Real Estate Services</li></ul></div>

<div class="abs" style="left:70px;top:4970px;width:1060px;height:1px;background:var(--line)"></div>
<p class="abs" style="left:144px;top:4986px;width:920px;font-size:11px;line-height:14px;color:var(--ink)">Lorem ipsum dolor sit amet, consectetur adipiscing elit, sed do eiusmod tempor incididunt ut labore et dolore magna aliqua. Quis ipsum suspendisse ultrices gravida. Risus commodo viverra maecenas accumsan lacus vel facilisis. Lorem ipsum dolor sit amet, consectetur adipiscing elit, sed do eiusmod tempor incididunt ut labore et dolore magna aliqua. Quis ipsum suspendisse ultrices gravida. Risus commodo viverra maecenas accumsan lacus vel facilisis.</p>
<p class="abs" style="left:144px;top:5050px;font-size:14px;color:var(--ink)">Copyright © 2023 &nbsp;|&nbsp; Privacy Policy</p>

</body>
</html>
```